Flyer-Design für ein Montessori Familienzentrum
Super Zusammenarbeit :) Meine Wünsche und Ideen wurden sehr passend und schnell umgesetzt und miteinbezogen in das Design.
Zielgruppe
Wir sind ein Montessori Familienzentrum mit folgendem Angebot:
- Montessori Eltern-Kind-Gruppen für Babys ab 8 Wochen - 4 Jahren
- Montessori Coaching
- Stoffwindel- und Windelfrei Beratung
- Beratung zur Babygeleiteten Beikost
- Workshops für Eltern
Aufgabenstellung
Schlicht, Informativ, Überblick über die Angebote

```html
<!DOCTYPE html>
<html lang="de">
<head>
<meta charset="utf-8">
<title>Montessori Familienzentrum – Flyer</title>
<link href="https://fonts.googleapis.com/css2?family=Jost:ital,wght@0,400;0,500;0,700;1,400;1,500;1,700&family=Libre+Baskerville:wght@400;700&family=Great+Vibes&display=swap" rel="stylesheet">
<style>
:root{
  --bg:#dcdcdc;
  --paper:#ffffff;
  --band:#efefef;
  --band-dark:#e4e4e4;
  --orange:#e8782f;
  --green:#4f8a2e;
  --text:#5a5a5a;
  --ink:#3c3c3c;
}
*{margin:0;padding:0;box-sizing:border-box}
html,body{width:959px;height:1200px;overflow:hidden;background:var(--bg)}
body{font-family:"Jost",sans-serif;color:var(--text);position:relative}
.spread{position:absolute;left:0;width:959px;height:470px;background:var(--paper);display:flex;box-shadow:0 4px 14px rgba(0,0,0,.15)}
.spread--inside{top:30px}
.spread--outside{top:560px}
.spread-bands{position:absolute;inset:0;width:100%;height:100%}
.panel{position:relative;width:319.67px;height:470px;overflow:hidden}
.panel + .panel{border-left:1px solid #e6e6e6}
.photo{position:absolute}
.title{font-weight:700;font-style:italic;color:var(--orange);font-size:17px;line-height:1.05}
.sub{font-style:italic;font-size:9px;color:var(--ink)}
.head{font-weight:500;color:var(--green);font-size:11.5px;letter-spacing:.3px;text-transform:uppercase}
.kicker{font-style:italic;color:var(--orange);font-size:8px}
.copy{font-size:6.8px;line-height:1.45;color:var(--text)}
.copy ul{list-style:none;margin-top:3px;padding-left:12px}
.copy li::before{content:"• "}
.block{position:absolute}
.brand{position:absolute;display:flex;align-items:center;gap:5px;font-weight:700;font-size:14px;color:var(--green)}
.brand-dot{width:10px;height:10px;border-radius:50%;background:var(--green)}
.footer-line{position:absolute;font-size:6.8px;letter-spacing:1px;color:var(--ink);text-transform:uppercase}
.cover-title{position:absolute;left:24px;top:322px;font-family:"Libre Baskerville",serif;color:var(--green);line-height:1}
.cover-title .big{font-size:27px;font-weight:700;letter-spacing:.5px}
.cover-title .small{font-size:19px;letter-spacing:1px;display:block;margin-top:3px}
.contact{position:absolute;left:24px;bottom:22px;font-size:6.4px;letter-spacing:.6px;color:var(--ink);text-transform:uppercase;display:flex;gap:10px}
.signature{position:absolute;font-family:"Great Vibes",cursive;font-size:16px;color:var(--ink)}
.label-side{position:absolute;right:120px;top:1148px;font-size:18px;font-weight:500;color:#4a2a3a;letter-spacing:.5px}
</style>
</head>
<body>

<!-- Innenseite -->
<section class="spread spread--inside">
  <svg class="spread-bands" viewBox="0 0 959 470" preserveAspectRatio="none" aria-hidden="true">
    <polygon points="0,250 320,150 320,330 0,420" fill="var(--band)"/>
    <polygon points="320,300 640,220 640,470 320,470" fill="var(--band)"/>
    <polygon points="640,150 959,60 959,280 640,370" fill="var(--band)"/>
  </svg>

  <article class="panel panel--playgroups">
    <div class="photo" role="img" aria-label="Foto: Mutter mit Brille hält ihr Baby im Arm" style="left:190px;top:0;width:130px;height:270px;border-radius:0 0 0 110px;background:linear-gradient(160deg,#e9dccb,#b98560 55%,#7a5a40)"></div>
    <div class="block" style="left:22px;top:22px">
      <h2 class="title">Spielgruppen für Babys</h2>
      <p class="sub" style="margin-left:60px">Ab 8 Wochen – 4 Jahre</p>
    </div>
    <div class="block" style="left:22px;top:82px;width:170px">
      <h3 class="head">Was ist Montessori?</h3>
      <p class="kicker" style="text-align:right">Informationen zum pädagogischen Konzept</p>
      <p class="copy">In den Gruppenstunden liegt der Schwerpunkt auf der Beobachtung des eigenen Kindes und der Eltern-Kind-Beziehung. Jedes Kind gestaltet seine Zeit ganz individuell nach seinen Bedürfnissen. Jede Gruppe hat einen eigenen Raum mit Montessori Material der Altersgruppe 0-3 Jahre sowie 3-6 Jahre.</p>
    </div>
    <div class="block" style="left:22px;top:192px;width:170px">
      <h3 class="head">Umsetzung Zuhause</h3>
      <p class="kicker" style="text-align:right">Anleitung der Eltern</p>
      <p class="copy">Zu jedem Thema bekommen die Eltern Unterstützung und Hilfestellung zur Umsetzung zu Hause. Im Elternportal der Website finden sie außerdem zusätzliche Tipps und Tricks.</p>
    </div>
    <div class="photo" role="img" aria-label="Foto: Kinder feiern ein Gartenfest mit Luftballons" style="left:-20px;top:290px;width:140px;height:130px;border-radius:50%;background:radial-gradient(circle at 40% 40%,#cfe0a8,#7fa24a 60%,#c68a4a)"></div>
    <div class="block" style="left:130px;top:318px;width:180px">
      <h3 class="head">Familien-Events</h3>
      <p class="kicker" style="text-align:right">Austausch und Vernetzung</p>
      <p class="copy">1x pro Kursblock findet ein Eltern-Event wie z.B. Eltern-Café, Sommerfest, Martinsumzug etc. statt. Die Eltern können sich mit Teilnehmern aus anderen Kursen austauschen.</p>
    </div>
    <p class="footer-line" style="left:22px;top:442px">Montessori Pädagogik für Babys und Kleinkinder</p>
  </article>

  <article class="panel panel--groups">
    <div class="photo" role="img" aria-label="Foto: Baby liegt auf einer hellen Decke" style="left:185px;top:0;width:135px;height:110px;border-radius:0 0 0 70px;background:linear-gradient(150deg,#f3e6e4,#e2c8c2 60%,#cfb0a8)"></div>
    <div class="photo" role="img" aria-label="Foto: Krabbelndes Baby lächelt" style="left:185px;top:115px;width:135px;height:150px;border-radius:70px 0 0 70px;background:linear-gradient(150deg,#b9cbd8,#e8c8a8 55%,#c7a07a)"></div>
    <div class="block" style="left:18px;top:22px">
      <h2 class="title" style="font-size:16px">Gruppeneinteilung</h2>
    </div>
    <div class="block" style="left:18px;top:62px;width:165px">
      <h3 class="head" style="color:var(--green)">Baby Kurse</h3>
      <p class="kicker" style="margin-left:20px">ab 8 Wochen bis 6 Monate</p>
      <p class="copy" style="margin-top:6px">Im Baby Kurs lernen die Teilnehmer unter anderem die verschiedenen Montessori Mobiles kennen. Wir sprechen über Themen wie z.B.: Ernährung, bedürfnisorientiertes Wickeln, Eingewöhnung in die KITA und noch vieles mehr.</p>
    </div>
    <div class="block" style="left:18px;top:170px;width:165px">
      <h3 class="head">Crawler Kurse</h3>
      <p class="kicker" style="margin-left:20px">ab 6 Monaten bis ca.15 Monate</p>
      <p class="copy" style="margin-top:6px">Im Crawler Kurs findet eine gemeinsame Brotzeit nach BLW statt. Ein Montessori Spiegel mit integrierter Pull-up-Stange lädt die Kinder zum Hochziehen ein.</p>
    </div>
  </article>

  <article class="panel panel--coaching">
    <div class="photo" role="img" aria-label="Foto: Heller Kindertisch mit Körben im Wohnraum" style="left:165px;top:0;width:155px;height:230px;border-radius:0 0 0 120px;background:linear-gradient(160deg,#f1ede6,#ddd2c2 55%,#b89a76)"></div>
    <div class="photo" role="img" aria-label="Foto: Holzregal mit Waschschüssel und Handtuch" style="left:20px;top:260px;width:140px;height:170px;background:linear-gradient(170deg,#e8e2d8,#d8bf95 55%,#8d7a68)"></div>
    <div class="block" style="left:18px;top:22px;width:150px">
      <h2 class="title" style="font-size:15px;font-style:normal">Montessori Coaching für Zuhause</h2>
      <p class="sub" style="font-style:normal;margin-left:34px;margin-top:4px">Ab Babyalter - Preschool Alter</p>
    </div>
    <div class="block" style="left:18px;top:100px;width:145px">
      <p class="copy">Wir gestalten zusammen Euer individuelles Zuhause nach den Prinzipien der Montessori Pädagogik.</p>
      <p class="copy" style="margin-top:8px;text-transform:uppercase">Wie läuft ein Montessori Coaching ab?</p>
      <p class="copy">Das Coaching besteht aus 3 Hausbesuchen, die jeweils ca. 2 Stunden dauern und sich über einen Zeitraum von 6-8 Wochen erstrecken.</p>
    </div>
    <div class="brand" style="left:196px;top:362px"><span class="brand-dot"></span>Kleinwurzel</div>
  </article>
</section>

<!-- Außenseite -->
<section class="spread spread--outside">
  <svg class="spread-bands" viewBox="0 0 959 470" preserveAspectRatio="none" aria-hidden="true">
    <polygon points="0,200 320,110 320,300 0,390" fill="var(--band)"/>
    <polygon points="320,330 640,260 640,470 320,470" fill="var(--band)"/>
    <polygon points="640,260 959,180 959,360 640,440" fill="var(--band)"/>
  </svg>

  <article class="panel panel--advice">
    <div class="photo" role="img" aria-label="Foto: Korb mit bunten Stoffwindeln" style="left:90px;top:0;width:210px;height:135px;border-radius:0 0 10px 10px;background:linear-gradient(160deg,#ececec,#8fc65a 40%,#e9c24a 65%,#9aa7b4)"></div>
    <div class="block" style="left:30px;top:168px;width:270px">
      <h2 class="title" style="font-size:15px">Weiter Beratungsangebote:</h2>
      <p class="sub" style="margin-left:40px;margin-top:6px;font-size:9.5px">Stoffwindel- und Windelfrei-Beratung:</p>
      <div class="copy" style="margin-left:40px;margin-top:3px">
        <p>Für alle Eltern, die sich für das Thema Stoffwindeln und Abhalten interessieren und gern mehr darüber erfahren möchten. Auch für (Stoff)-Eltern, die Probleme haben oder etwas Neues ausprobieren wollen.</p>
        <ul><li>Einzel- Paarberatung</li><li>Workshops</li><li>Stoffwindelparty</li><li>Problemanalysen</li><li>Miet- und Testpakete (ab Geburt – Trocken werden)</li></ul>
      </div>
    </div>
    <div class="photo" role="img" aria-label="Foto: Tablett mit gemusterter Stoffwindel und Pflegedose" style="left:0;top:358px;width:115px;height:92px;background:linear-gradient(160deg,#c9453a,#e9e3da 60%,#cfc6b8)"></div>
    <div class="block" style="left:130px;top:362px;width:180px">
      <p class="sub" style="font-size:9px">Beratung rund ums Thema:<br>Babygeleitete Beikost</p>
      <div class="copy" style="margin-top:3px">
        <p>Du möchtest wissen, was genau BLW ist und wie man es am besten umsetzt? Oder setzt es schon um, kommst aber nicht weiter? Dann ist eine individuelle Beratung genau das Richtige!</p>
        <ul><li>Einzelberatungen</li><li>Workshops</li></ul>
      </div>
    </div>
  </article>

  <article class="panel panel--about">
    <div class="block copy" style="left:16px;top:32px;width:130px;font-size:6.3px">
      <p>Hallo,<br>mein Name ist Lena, ich bin Jahrgang 1994, verheiratet und wohne mit meiner Familie in Auental. Ich bin staatlich anerkannte Erzieherin und habe nach meiner Ausbildung zunächst ein Jahr in Amerika gelebt und gearbeitet und danach in einer normalen und einer integrativen Kinderkrippe. Kleinwurzel habe ich im September 2020 gegründet und seit September 2021 hat das Kurskonzept einen Montessori Schwerpunkt. Neben meiner Fortbildung zur Montessori Spielgruppenleiterin mache ich derzeit noch das Montessori Diplom für Kleinkinder. Ich bin außerdem zertifizierte Stoffwindelberaterin, Windelfrei Coach und Fachkraft für Babygeleitete Beikost (BLW). Ich freue mich Euch in einem meiner Kurse kennenzulernen.</p>
    </div>
    <p class="signature" style="left:60px;top:252px">Eure Lena</p>
    <div class="photo" role="img" aria-label="Foto: Familie mit Kind auf den Schultern im Feld" style="left:160px;top:0;width:150px;height:290px;border-radius:0 0 75px 75px;background:linear-gradient(170deg,#c9c4cc,#b8845c 40%,#8a5a3a 70%,#6e4a36)"></div>
    <div class="brand" style="left:26px;top:360px"><span class="brand-dot"></span>Kleinwurzel</div>
    <div class="block" style="left:150px;top:340px;width:160px">
      <h3 style="font-weight:400;font-size:11px;letter-spacing:1px;color:var(--ink)">LENA BRANDT</h3>
      <p class="copy" style="margin-left:28px;margin-top:4px;font-size:6.4px">Staatlich anerkannte Erzieherin ·<br>Diplom Montessori Pädagogin i.A.<br>zertifizierte Stoffwindelberaterin /<br>Abhalte- und Windelfrei Coach,<br>Fachkraft für Babygeleitete Beikost</p>
    </div>
  </article>

  <article class="panel panel--cover">
    <div class="photo" role="img" aria-label="Foto: Offene Hände halten eine Papierfamilie" style="left:100px;top:0;width:220px;height:300px;border-radius:0 0 0 150px;background:linear-gradient(160deg,#f3e1d6,#e2a98e 45%,#c47e60 80%,#a8654a)"></div>
    <div class="brand" style="left:22px;top:36px"><span class="brand-dot"></span>Kleinwurzel</div>
    <div class="cover-title"><span class="big">MONTESSORI</span><span class="small">Familienzentrum</span></div>
    <p class="footer-line" style="left:24px;top:378px;font-size:6.4px">Montessori Pädagogik für Babys und Kleinkinder</p>
    <p class="footer-line" style="left:190px;top:394px;font-size:6.4px;color:var(--orange)">Ab 8 Wochen bis 4 Jahre</p>
    <div class="contact"><span>info@kleinwurzel.de</span><span>www.kleinwurzel.de</span><span>kleinwurzel</span><span>kleinwurzel</span></div>
  </article>
</section>

<p class="label-side">AUSSEN</p>

</body>
</html>
```